Business Card for a Dental Office

The design should communicate integrity, quality and reliability. We also want the card look elegant, simple, but still stand out, different from the traditional-dental-office business card.

Business

```html
<!DOCTYPE html>
<html lang="en">
<head>
<meta charset="utf-8">
<title>Larkfield Dental Studio – Business Card</title>
<link rel="stylesheet" href="https://fonts.googleapis.com/css2?family=Open+Sans:wght@400;600;700&display=swap">
<style>
  :root {
    --backdrop: #e4e4e2;
    --card-white: #ffffff;
    --charcoal: #39393b;
    --gold: #cdb424;
    --ink: #1d1d1d;
    --light-text: #f2f2f2;
  }
  * { margin: 0; padding: 0; box-sizing: border-box; }
  html, body {
    width: 1200px;
    height: 977px;
    overflow: hidden;
    background: var(--backdrop);
    font-family: "Open Sans", sans-serif;
  }
  .business-card {
    position: absolute;
    left: 100px;
    top: 202px;
    width: 1000px;
    height: 572px;
    background: var(--card-white);
    box-shadow: 0 10px 30px rgba(0,0,0,0.18);
    overflow: hidden;
  }
  .card-shapes {
    position: absolute;
    inset: 0;
    width: 100%;
    height: 100%;
  }
  .contact-panel {
    position: absolute;
    left: 112px;
    top: 150px;
    color: var(--light-text);
  }
  .holder-name {
    color: var(--gold);
    font-size: 34px;
    font-weight: 600;
    line-height: 1.1;
  }
  .holder-role {
    font-size: 19px;
    font-weight: 700;
    margin: 4px 0 0 10px;
  }
  .contact-list {
    list-style: none;
    margin: 34px 0 0 28px;
    font-size: 19px;
    line-height: 1.5;
  }
  .contact-item {
    display: flex;
    align-items: flex-start;
    gap: 14px;
  }
  .contact-item + .contact-item { margin-top: 2px; }
  .contact-item.address { margin-bottom: 24px; }
  .contact-icon {
    width: 20px;
    height: 20px;
    flex: none;
    margin-top: 5px;
    fill: var(--gold);
  }
  .brand-lockup {
    position: absolute;
    left: 590px;
    top: 222px;
    display: flex;
    align-items: center;
    gap: 12px;
    white-space: nowrap;
  }
  .brand-mark {
    width: 40px;
    height: 40px;
    background: var(--gold);
  }
  .brand-name {
    color: var(--ink);
    font-size: 23px;
    font-weight: 700;
    letter-spacing: 0.2px;
    line-height: 1;
  }
</style>
</head>
<body>
  <article class="business-card">
    <svg class="card-shapes" viewBox="0 0 1000 572" aria-hidden="true">
      <path class="dark-field" fill="var(--charcoal)"
        d="M0,0 H330 C470,60 565,250 522,420 C506,485 488,535 470,572 H0 Z"/>
      <path class="gold-arc" fill="none" stroke="var(--gold)" stroke-width="4.5" stroke-linecap="round"
        d="M352,6 C497,80 590,262 546,430 C536,470 526,505 512,540"/>
    </svg>

    <section class="contact-panel">
      <h1 class="holder-name">Daniel Hartley</h1>
      <p class="holder-role">Manager</p>
      <ul class="contact-list">
        <li class="contact-item address">
          <svg class="contact-icon" viewBox="0 0 20 20"><path d="M10 1a6 6 0 0 0-6 6c0 4.5 6 12 6 12s6-7.5 6-12a6 6 0 0 0-6-6zm0 8.3A2.3 2.3 0 1 1 10 4.7a2.3 2.3 0 0 1 0 4.6z"/></svg>
          <span>1234 Maple Avenue,<br>CA 95021</span>
        </li>
        <li class="contact-item phone">
          <svg class="contact-icon" viewBox="0 0 20 20"><path d="M5.2 2.5l2.6 3.1-1.6 2a11 11 0 0 0 6.2 6.2l2-1.6 3.1 2.6-1.7 2.7C9.4 17.7 2.3 10.6 2.5 4.2z"/></svg>
          <span>(800) 555-0142</span>
        </li>
        <li class="contact-item email">
          <svg class="contact-icon" viewBox="0 0 20 20"><path d="M2 4h16v1.6l-8 5-8-5zM2 7.8l8 5 8-5V16H2z"/></svg>
          <span>info@larkfield.com</span>
        </li>
        <li class="contact-item web">
          <svg class="contact-icon" viewBox="0 0 20 20"><path d="M10 1.5a8.5 8.5 0 1 0 0 17 8.5 8.5 0 0 0 0-17zm5.9 7.7h-2.6a13 13 0 0 0-1-5 6.9 6.9 0 0 1 3.6 5zM10 3.2c.8 1 1.5 3.2 1.7 6H8.3c.2-2.8.9-5 1.7-6zm-2.3 1a13 13 0 0 0-1 5H4.1a6.9 6.9 0 0 1 3.6-5zm-3.6 6.6h2.6a13 13 0 0 0 1 5 6.9 6.9 0 0 1-3.6-5zm5.9 6c-.8-1-1.5-3.2-1.7-6h3.4c-.2 2.8-.9 5-1.7 6zm2.3-1a13 13 0 0 0 1-5h2.6a6.9 6.9 0 0 1-3.6 5z"/></svg>
          <span>www.larkfield.com</span>
        </li>
      </ul>
    </section>

    <div class="brand-lockup">
      <span class="brand-mark" aria-hidden="true"></span>
      <span class="brand-name">LARKFIELD DENTAL STUDIO</span>
    </div>
  </article>
</body>
</html>
```